The Willow Hours - a modern wellness brand

Looking for a modern, simple, and clean website for a virtual consulting firm focused on holistic wellness and sustainable living. Want a strong combo of text and photos (really shitty starts are available for reference on www.thewillowhours.com and www.helenabrusco.com for reference - general idea is in the right direction, was too difficult to work through with the wordpress template and nothing laid out correctly)
Needs include:
- strong home / landing page
- ability to schedule (use calend.ly) on the site
- online shop / purchasing POS integration
- blog
-multiple 'services' pages
- about page
- contact page
(attached brand board images for brand style / reference)
Updates
Want more opportunity for designs and feedback
Target Market(s)
women and gay men aged 30-50
Coding
Coded - Design and coding required
Number of Pages Required
5+ page
Colors
Designer to choose only greyscale colors for use in the design.
Requirements
Must have
- the ability for me to update and manage through wordpress when things like pricing, or services change
Should not have
- complicated anything

```html
<!DOCTYPE html>
<html lang="en">
<head>
<meta charset="utf-8">
<title>The Willow Hours</title>
<link href="https://fonts.googleapis.com/css2?family=Playfair+Display:wght@400;700&family=Poppins:wght@400;500;600&display=swap" rel="stylesheet">
<style>
:root{
  --ink:#231f20;
  --text:#3a3a3a;
  --muted:#6b6b6b;
  --accent:#464646;
  --accent-soft:#7c7c7c;
  --icon:#5a5a5a;
  --paper:#ffffff;
  --line:#d9d9d9;
  --dot:#e2e2e2;
}
*{margin:0;padding:0;box-sizing:border-box}
html,body{width:1200px;height:3916px;overflow:hidden;background:var(--paper)}
body{position:relative;font-family:'Poppins',sans-serif;color:var(--text)}
.abs{position:absolute}
.serif{font-family:'Playfair Display',serif}
.photo{position:absolute}
h1,h2,h3,h4,h5{font-weight:400}

/* header */
.brand{position:absolute;left:88px;top:22px;display:flex;align-items:center;gap:14px}
.brand-dot{width:58px;height:58px;border:1.5px solid var(--ink);border-radius:50%}
.brand-name{font-size:19px;letter-spacing:5px;color:var(--ink);font-weight:400;white-space:nowrap}
.nav{position:absolute;left:455px;top:32px;display:flex;align-items:center;gap:28px;font-size:14px;color:var(--ink)}
.btn-dark{position:absolute;background:var(--ink);color:#fff;font-size:11px;font-weight:600;display:flex;align-items:center;justify-content:center;letter-spacing:.2px}

/* hero */
.hero-title{left:86px;top:210px;font-size:82px;line-height:80px;color:var(--ink)}
.hero-sub{left:88px;top:468px;width:340px;font-size:14px;line-height:21px}

.dots{position:absolute;display:grid;gap:7px}
.dots span{width:7px;height:7px;border-radius:50%;background:var(--dot)}

.section-title{position:absolute;left:0;width:1200px;text-align:center;font-size:40px;font-weight:400;color:var(--ink);font-family:'Playfair Display',serif;white-space:nowrap}

/* services */
.service{position:absolute;width:260px;text-align:center}
.service .icon{width:84px;height:72px;margin:0 auto;border-radius:10px;background:#efefef}
.service h3{font-family:'Playfair Display',serif;font-weight:700;font-size:17px;letter-spacing:.5px;color:var(--ink);margin-top:18px}
.service p{font-size:12px;line-height:18px;margin-top:10px}

/* about */
.about-title{left:508px;top:1338px;font-size:41px;line-height:44px;color:var(--ink);white-space:nowrap}
.about-text{left:508px;top:1446px;width:500px;font-size:13.8px;line-height:22.5px}

/* band */
.band{position:absolute;left:0;top:1893px;width:1200px;height:428px;background:var(--accent)}
.ghost{position:absolute;left:0;width:1200px;text-align:center;top:1990px;font-family:'Playfair Display',serif;font-weight:700;font-size:100px;color:rgba(255,255,255,.06);letter-spacing:2px}
.btn-light{position:absolute;background:#fff;color:var(--ink);font-size:13px;font-weight:600;display:flex;align-items:center;justify-content:center}

/* blog */
.card{position:absolute;top:2508px;width:295px;height:387px;background:#fff;box-shadow:0 10px 30px rgba(0,0,0,.06)}
.card .photo{position:static;width:295px;height:235px}
.card .body{padding:18px 29px}
.card time{font-size:11px;font-weight:500;color:var(--ink)}
.card h4{font-family:'Playfair Display',serif;font-weight:700;font-size:14px;margin-top:12px;color:var(--ink)}
.card p{font-size:12px;line-height:17px;margin-top:8px}

/* testimonial */
.quote-mark{left:650px;top:2880px;font-family:'Playfair Display',serif;font-size:320px;line-height:1;color:#f2f2f2}
.quote{left:458px;top:3060px;width:590px;font-size:22.5px;line-height:36px;color:var(--ink)}
.cite{left:458px;top:3236px;font-family:'Playfair Display',serif;font-weight:700;font-size:12px;color:var(--accent)}

/* footer */
.footer{position:absolute;left:0;top:3443px;width:1200px;height:473px;background:var(--ink)}
.newsletter{position:absolute;left:664px;top:3357px;width:536px;height:188px;background:var(--accent)}
.newsletter h5{position:absolute;left:60px;top:40px;font-family:'Playfair Display',serif;font-weight:700;font-size:15px;color:#fff}
.field{position:absolute;left:62px;top:63px;width:298px;height:48px;background:#fff;display:flex;align-items:center;padding-left:18px;gap:10px;font-size:13px;color:#999}
.subscribe{position:absolute;left:360px;top:63px;width:104px;height:48px;background:var(--ink);border:2px solid #fff;color:#fff;font-size:12px;font-weight:600;display:flex;align-items:center;justify-content:center}
.f-title{font-family:'Playfair Display',serif;font-weight:700;font-size:18px;color:#fff}
.links{list-style:none;font-size:12px;color:#fff}
.links li{height:31px}
.links li::before{content:"›";color:#888;margin-right:8px}
.contact{font-size:12px;color:#fff;line-height:17px}
.contact .row{display:flex;gap:10px;margin-bottom:18px}
.social{position:absolute;width:38px;height:38px;border-radius:50%;background:#3a3637}
.footer-line{position:absolute;left:88px;top:3870px;width:1022px;height:1px;background:#444}
.fine{font-size:11px;color:#fff}
.footer-brand{position:absolute;left:100px;top:3625px;width:320px;text-align:center}
.footer-brand .mark{width:96px;height:96px;border:1.5px solid #fff;border-radius:50%;margin:0 auto 24px}
.footer-brand .name{font-size:22px;letter-spacing:4px;color:#fff;white-space:nowrap}
</style>
</head>
<body>

<header>
  <div class="brand"><span class="brand-dot"></span><span class="brand-name">THE WILLOW HOURS</span></div>
  <nav class="nav">
    <svg width="16" height="14" viewBox="0 0 16 14"><path d="M8 0L0 7h2v7h4V9h4v5h4V7h2z" fill="#464646"/></svg>
    <span>About</span><span>Services</span><span>Online Shop</span><span>Blog</span><span>Contact</span>
    <svg width="30" height="28" viewBox="0 0 30 28" fill="none" stroke="#231f20" stroke-width="2"><path d="M1 4h5l3 14h15l3-10H8"/><circle cx="11" cy="24" r="2"/><circle cx="22" cy="24" r="2"/><circle cx="26" cy="4" r="3.5" fill="#7c7c7c" stroke="none"/></svg>
  </nav>
  <a class="btn-dark" style="left:955px;top:23px;width:155px;height:42px">ABILITY TO SCHEDULE</a>
</header>

<section>
  <h1 class="abs serif hero-title">THE<br>WILLOW<br>HOURS</h1>
  <p class="abs hero-sub">For a virtual consulting firm focused on holistic wellness and sustainable living.</p>
  <div class="dots" style="left:430px;top:615px;grid-template-columns:repeat(8,7px)">
    <span></span><span></span><span></span><span></span><span></span><span></span><span></span><span></span>
    <span></span><span></span><span></span><span></span><span></span><span></span><span></span><span></span>
    <span></span><span></span><span></span><span></span><span></span><span></span><span></span><span></span>
    <span></span><span></span><span></span><span></span><span></span><span></span><span></span><span></span>
    <span></span><span></span><span></span><span></span><span></span><span></span><span></span><span></span>
    <span></span><span></span><span></span><span></span><span></span><span></span><span></span><span></span>
    <span></span><span></span><span></span><span></span><span></span><span></span><span></span><span></span>
    <span></span><span></span><span></span><span></span><span></span><span></span><span></span><span></span>
  </div>
  <div class="photo" role="img" aria-label="Group of women doing a tree yoga pose on a misty beach" style="left:487px;top:97px;width:713px;height:574px;background:linear-gradient(180deg,#c7ced3 0%,#a9b3b8 40%,#b7aa98 62%,#9c8e7c 100%)"></div>
</section>

<section>
  <h2 class="section-title" style="top:805px">OUR SERVICES</h2>
  <div class="service" style="left:152px;top:880px"><div class="icon" role="img" aria-label="Coaching icon"></div><h3>COACHING</h3><p>Consulting firm focused on holistic<br>wellness &amp; sustainable living.</p></div>
  <div class="service" style="left:470px;top:880px"><div class="icon" role="img" aria-label="Training icon"></div><h3>TRAINING</h3><p>Consulting firm focused on holistic<br>wellness &amp; sustainable living.</p></div>
  <div class="service" style="left:788px;top:880px"><div class="icon" role="img" aria-label="Food icon"></div><h3>FOOD</h3><p>Consulting firm focused on holistic<br>wellness &amp; sustainable living.</p></div>
  <div class="service" style="left:152px;top:1068px"><div class="icon" role="img" aria-label="Physiotherapy icon"></div><h3>PHYSIOTHERAPY</h3><p>Consulting firm focused on holistic<br>wellness &amp; sustainable living.</p></div>
  <div class="service" style="left:470px;top:1068px"><div class="icon" role="img" aria-label="Motivation icon"></div><h3>MOTIVATION</h3><p>Consulting firm focused on holistic<br>wellness &amp; sustainable living.</p></div>
  <div class="service" style="left:788px;top:1068px"><div class="icon" role="img" aria-label="Support icon"></div><h3>SUPPORT</h3><p>Consulting firm focused on holistic<br>wellness &amp; sustainable living.</p></div>
</section>

<section>
  <div class="photo" role="img" aria-label="Two women laughing together on a bed in a bright room" style="left:0;top:1335px;width:400px;height:608px;background:linear-gradient(160deg,#d8d2cc 0%,#bfae9e 45%,#e2c3b3 100%)"></div>
  <h2 class="abs serif about-title">ABOUT<br>THE WILLOW HOURS</h2>
  <p class="abs about-text">Aenean sollicitudin, lorem quis bibendum auctor, nisi elit consequat ipsum, nec sagittis sem nibh id elit. Duis sed odio sit amet nibh vulputate cursus a sit amet mauris. Morbi accumsan ipsum velit. Nam nec tellus a tincidunt auctor a ornare odio. Sed non &nbsp;mauris vitae erat consequat auctor eu in elit. Class aptent taciti...</p>
  <a class="btn-dark" style="left:508px;top:1589px;width:143px;height:42px">FIND OUT MORE</a>
  <div class="abs" style="left:508px;top:1722px;width:327px;height:1px;background:var(--line)"></div>
  <div class="photo" role="img" aria-label="Hands preparing blueberry toasts on a wooden board" style="left:904px;top:1598px;width:296px;height:217px;background:linear-gradient(135deg,#f0eeeb 0%,#d9c7b0 55%,#b9a38a 100%)"></div>
</section>

<section>
  <div class="band"></div>
  <div class="dots" style="left:320px;top:1897px;grid-template-columns:repeat(11,7px);gap:5px 6px">
    <span style="visibility:hidden"></span><span style="visibility:hidden"></span><span style="visibility:hidden"></span><span style="visibility:hidden"></span><span style="visibility:hidden"></span><span style="visibility:hidden"></span><span style="visibility:hidden"></span><span style="background:var(--accent-soft)"></span><span style="background:var(--accent-soft)"></span><span style="background:var(--accent-soft)"></span><span style="background:var(--accent-soft)"></span>
    <span style="visibility:hidden"></span><span style="visibility:hidden"></span><span style="visibility:hidden"></span><span style="visibility:hidden"></span><span style="visibility:hidden"></span><span style="visibility:hidden"></span><span style="visibility:hidden"></span><span style="background:var(--accent-soft)"></span><span style="background:var(--accent-soft)"></span><span style="background:var(--accent-soft)"></span><span style="background:var(--accent-soft)"></span>
    <span style="visibility:hidden"></span><span style="visibility:hidden"></span><span style="visibility:hidden"></span><span style="visibility:hidden"></span><span style="visibility:hidden"></span><span style="visibility:hidden"></span><span style="visibility:hidden"></span><span style="background:var(--accent-soft)"></span><span style="background:var(--accent-soft)"></span><span style="background:var(--accent-soft)"></span><span style="background:var(--accent-soft)"></span>
    <span style="background:var(--accent-soft)"></span><span style="background:var(--accent-soft)"></span><span style="background:var(--accent-soft)"></span><span style="background:var(--accent-soft)"></span><span style="background:var(--accent-soft)"></span><span style="background:var(--accent-soft)"></span><span style="background:var(--accent-soft)"></span><span style="background:var(--accent-soft)"></span><span style="background:var(--accent-soft)"></span><span style="background:var(--accent-soft)"></span><span style="background:var(--accent-soft)"></span>
    <span style="background:var(--accent-soft)"></span><span style="background:var(--accent-soft)"></span><span style="background:var(--accent-soft)"></span><span style="background:var(--accent-soft)"></span><span style="background:var(--accent-soft)"></span><span style="background:var(--accent-soft)"></span><span style="background:var(--accent-soft)"></span><span style="background:var(--accent-soft)"></span><span style="background:var(--accent-soft)"></span><span style="background:var(--accent-soft)"></span><span style="background:var(--accent-soft)"></span>
  </div>
  <div class="ghost">WILLOW</div>
  <h2 class="section-title" style="top:2098px;color:#fff">PURCHASING POS INTEGRATION</h2>
  <a class="btn-light" style="left:498px;top:2172px;width:205px;height:42px">ONLINE SHOPPING</a>
</section>

<section>
  <h2 class="section-title" style="top:2395px">LATEST BLOG</h2>
  <p class="abs" style="left:0;width:1200px;text-align:center;top:2455px;font-size:12px">Consulting firm focused on holistic wellness &amp; sustainable living.</p>
  <article class="card" style="left:138px">
    <div class="photo" role="img" aria-label="Woman stretching beside indoor plants" style="background:linear-gradient(135deg,#d9d5cc,#8f9a7c 45%,#efe9e2)"></div>
    <div class="body"><time>25-05-2022</time><h4>SOME HEADING GOES HERE</h4><p>Aenean sollicitudin, lorem quis nisi elit consequat ipsum nec sagittis sem nibh id elit duis sed odio...</p></div>
  </article>
  <article class="card" style="left:452px">
    <div class="photo" role="img" aria-label="Open book, coffee and glasses on linen" style="background:linear-gradient(135deg,#e7e3e6,#d8d3d6 50%,#f1eeef)"></div>
    <div class="body"><time>25-05-2022</time><h4>SOME HEADING GOES HERE</h4><p>Aenean sollicitudin, lorem quis nisi elit consequat ipsum nec sagittis sem nibh id elit duis sed odio...</p></div>
  </article>
  <article class="card" style="left:767px">
    <div class="photo" role="img" aria-label="Woman meditating on a yoga mat seen from above" style="background:linear-gradient(135deg,#c9a27e,#2f5a5c 50%,#b99272)"></div>
    <div class="body"><time>25-05-2022</time><h4>SOME HEADING GOES HERE</h4><p>Aenean sollicitudin, lorem quis nisi elit consequat ipsum nec sagittis sem nibh id elit duis sed odio...</p></div>
  </article>
</section>

<section>
  <div class="abs quote-mark">“</div>
  <div class="photo" role="img" aria-label="Portrait of the founder" style="left:163px;top:3035px;width:255px;height:255px;border-radius:50%;background:radial-gradient(circle at 50% 40%,#ead8c8,#d9d4cf 70%)"></div>
  <p class="abs quote">“Doing the work to help ourselves to see and know our own worth, our power and our purpose enables us to see and know others more purposefully and fully as humans.”</p>
  <p class="abs cite">— HELENA BRUSCO , FOUNDER OF THE WILLOW HOURS</p>
</section>

<footer>
  <div class="footer"></div>
  <div class="newsletter">
    <h5>SUBSCRIBE OUR NEWSLETTER</h5>
    <div class="field"><svg width="14" height="11" viewBox="0 0 14 11"><rect width="14" height="11" fill="#aaa"/><path d="M0 0l7 6 7-6" stroke="#fff" fill="none"/></svg>Enter email address...</div>
    <div class="subscribe">SUBSCRIBE</div>
  </div>

  <div class="footer-brand">
    <div class="mark"></div>
    <div class="name">THE WILLOW HOURS</div>
  </div>

  <div class="abs" style="left:472px;top:3590px">
    <div class="f-title">QUICK LINKS</div>
    <ul class="links" style="margin-top:22px">
      <li>Home</li><li>About Us</li><li>Services</li><li>Online Shop</li><li>Latest Blog</li><li>Contact</li>
    </ul>
  </div>

  <div class="abs" style="left:655px;top:3590px">
    <div class="f-title">CONTACT INFO</div>
    <div class="contact" style="margin-top:22px">
      <div class="row"><svg width="13" height="10" viewBox="0 0 13 10"><rect width="13" height="10" fill="#8a8a8a"/></svg><div>Email:<br>info@example.com</div></div>
      <div class="row"><svg width="13" height="13" viewBox="0 0 13 13"><path d="M3 0l2 3-1.5 1.5a8 8 0 005 5L10 8l3 2-1.5 3C5 12 1 8 0 1.5z" fill="#8a8a8a"/></svg><div>Phone:<br>+08 123 456 7890</div></div>
      <div class="row"><svg width="11" height="14" viewBox="0 0 11 14"><path d="M5.5 0A5.5 5.5 0 000 5.5C0 9 5.5 14 5.5 14S11 9 11 5.5A5.5 5.5 0 005.5 0z" fill="#8a8a8a"/><circle cx="5.5" cy="5.5" r="2" fill="#231f20"/></svg><div>Location:<br>Some address line here<br>United Kingdom</div></div>
    </div>
  </div>

  <span class="social" style="left:896px;top:3666px"></span>
  <span class="social" style="left:944px;top:3666px"></span>
  <span class="social" style="left:992px;top:3666px"></span>
  <span class="social" style="left:1039px;top:3666px"></span>

  <div class="footer-line"></div>
  <p class="abs fine" style="left:0;width:1200px;text-align:center;top:3886px;font-weight:600">© COPYRIGHT 2022 ALL RIGHTS RESERVED</p>
  <p class="abs fine" style="left:899px;top:3886px">Privacy Policy</p>
  <p class="abs fine" style="left:998px;top:3886px">Terms &amp; Conditions</p>
  <div class="abs" style="left:1133px;top:3850px;width:40px;height:40px;border-radius:50%;background:var(--accent);display:flex;align-items:center;justify-content:center">
    <svg width="10" height="14" viewBox="0 0 10 14" fill="none" stroke="#fff" stroke-width="1.5"><path d="M5 14V1M1 5l4-4 4 4"/></svg>
  </div>
</footer>

</body>
</html>
```